Maple Ridge business card design

Card needs to include the following text/items:
Company Logo
Tobin Marsh
Phone # - 555-318-7642
service@mapleridgelandscaping.example
Lawn & landscape maintenance services

```html
<!DOCTYPE html>
<html lang="en">
<head>
<meta charset="utf-8">
<title>Maple Ridge Landscaping – Business Card</title>
<link rel="stylesheet" href="https://fonts.googleapis.com/css2?family=Lato:wght@400;700;900&display=swap">
<style>
  :root {
    --backdrop: #cbcbcb;
    --forest: #22643a;
    --leaf: #5aa845;
    --sky: #9fd3e0;
    --arc-grey: #6f6e73;
    --paper: #ffffff;
    --muted: #6b6b6b;
  }
  * { box-sizing: border-box; margin: 0; padding: 0; }
  html, body { width: 1200px; height: 800px; overflow: hidden; }
  body {
    background: var(--backdrop);
    font-family: "Lato", "Helvetica Neue", Arial, sans-serif;
    position: relative;
  }
  .card {
    position: absolute;
    left: 390px;
    width: 420px;
    height: 240px;
    border-radius: 14px;
    overflow: hidden;
    box-shadow: 2px 3px 6px rgba(0,0,0,0.25);
  }
  .card--front { top: 130px; background: var(--paper); }
  .card--back  { top: 430px; background: var(--forest); }

  .card__wave { position: absolute; inset: 0; width: 100%; height: 100%; }

  .holder { position: absolute; left: 34px; top: 32px; }
  .holder__name {
    color: var(--forest);
    font-weight: 900;
    font-size: 20px;
    letter-spacing: 0.2px;
    line-height: 1;
  }
  .holder__role {
    color: var(--muted);
    font-size: 11px;
    margin-top: 6px;
  }

  .brand {
    position: absolute;
    display: flex;
    flex-direction: column;
    align-items: center;
  }
  .brand__disc {
    border-radius: 50%;
    background: linear-gradient(180deg, var(--sky) 0%, var(--leaf) 55%, var(--forest) 100%);
    border: 2px solid var(--leaf);
  }
  .brand__name {
    font-weight: 700;
    white-space: nowrap;
    line-height: 1;
  }
  .card--front .brand { left: 256px; top: 33px; width: 120px; }
  .card--front .brand__disc { width: 90px; height: 90px; }
  .card--front .brand__name { color: var(--forest); font-size: 20px; margin-top: 4px; }

  .card--back .brand { left: 110px; top: 38px; width: 200px; }
  .card--back .brand__disc { width: 108px; height: 108px; }
  .card--back .brand__name { color: var(--paper); font-size: 25px; margin-top: 8px; }

  .contacts {
    position: absolute;
    left: 32px;
    top: 162px;
    list-style: none;
  }
  .contacts__item {
    display: flex;
    align-items: center;
    color: var(--paper);
    font-size: 12px;
    height: 19px;
  }
  .contacts__icon { width: 12px; height: 12px; margin-right: 10px; flex: none; }

  .services {
    position: absolute;
    left: 0; right: 0;
    top: 197px;
    height: 19px;
    background: var(--paper);
    color: var(--forest);
    font-size: 10px;
    display: flex;
    align-items: center;
    justify-content: center;
    white-space: nowrap;
  }
</style>
</head>
<body>

<section class="card card--front">
  <svg class="card__wave" viewBox="0 0 700 400" preserveAspectRatio="none" aria-hidden="true">
    <path fill="var(--arc-grey)" d="M0 205 C60 160 120 147 160 147 C250 150 320 200 372 243 C310 195 240 172 160 172 C110 172 50 195 0 223 Z"/>
    <path fill="var(--forest)" d="M0 223 C60 185 120 168 160 170 C260 172 330 230 420 280 C480 312 520 320 545 318 C610 316 660 280 700 208 L700 400 L0 400 Z"/>
  </svg>

  <div class="holder">
    <h1 class="holder__name">TOBIN MARSH</h1>
    <p class="holder__role">Founder</p>
  </div>

  <div class="brand">
    <div class="brand__disc" role="img" aria-label="Round company emblem area with a landscape scene of trees, hills and sun"></div>
    <span class="brand__name">Maple Ridge</span>
  </div>

  <ul class="contacts">
    <li class="contacts__item">
      <svg class="contacts__icon" viewBox="0 0 24 24" aria-hidden="true"><path fill="#fff" d="M6.6 10.8a15.1 15.1 0 0 0 6.6 6.6l2.2-2.2a1 1 0 0 1 1-.25 11.4 11.4 0 0 0 3.6.57 1 1 0 0 1 1 1V20a1 1 0 0 1-1 1A17 17 0 0 1 3 4a1 1 0 0 1 1-1h3.5a1 1 0 0 1 1 1c0 1.25.2 2.45.57 3.57a1 1 0 0 1-.25 1z"/></svg>
      555-318-7642
    </li>
    <li class="contacts__item">
      <svg class="contacts__icon" viewBox="0 0 24 24" aria-hidden="true"><path fill="#fff" d="M2 5h20v14H2z"/><path fill="none" stroke="var(--forest)" stroke-width="1.6" d="M2 5l10 8 10-8M2 19l7-6M22 19l-7-6"/></svg>
      service@mapleridgelandscaping.example
    </li>
    <li class="contacts__item">
      <svg class="contacts__icon" viewBox="0 0 24 24" aria-hidden="true"><g fill="none" stroke="#fff" stroke-width="1.6"><circle cx="12" cy="12" r="10"/><ellipse cx="12" cy="12" rx="4.5" ry="10"/><path d="M2 12h20M4 7h16M4 17h16"/></g></svg>
      www.mapleridgelandscaping.example
    </li>
  </ul>
</section>

<section class="card card--back">
  <div class="brand">
    <div class="brand__disc" role="img" aria-label="Round company emblem area with a landscape scene of trees, hills and sun"></div>
    <span class="brand__name">Maple Ridge</span>
  </div>
  <p class="services">Lawn Mowing Service&nbsp; || &nbsp;Raking Service&nbsp; || &nbsp;Trimming &amp; Edging&nbsp; || &nbsp;Basic Gardening.</p>
</section>

</body>
</html>
```